Marriage Retreat: 4 Page Color Brochure

I need a 4 page, full color brochure that is 8.5 x 11 when folded (11 x 17 front/back when printed/unfolded). The brochure is to inform pastors and religious leaders about a private retreat to help them strengthen their marriages. Attached you will find: (1) a Word document with the copy/text and initial guidelines on the page layout (although some flexibility on what text goes on which page is acceptable); (2) a creative brief PDF with some of the visual ideas I have to jumpstart your thinking; (3) logo files for the organization Kindred Hearth (the logo must be included); (4) original scan of tree artwork that can be used as a visual element (this is the same tree that has been converted to a vector file in the logo; please use a color scheme in the brochure that is complementary to this artwork). The overall feel for this piece should be timeless, classic, welcoming and approachable. The font in the logo is Audrey, although it has been stylized a bit. Please take that into account when selecting fonts for the layout. I do not yet have the photo of Gus & Norah (the hosts of this retreat) for you to include with their bios. Please insert a placeholder image for now and I will get you the actual photo in a few days. Once we get to the final stage, I would also like to have a version of the file that is laid out as 4 individual 8.5x11 pages so it can be printed in that format if needed. I would also like to have a PDF version of each file.

Target Market(s)

The initial target market for this type of service will be males (who typically recommend the service to couples), but the ultimate decision maker will probably be a female (the wife of the couple that will attend the retreat).

Industry/Entity Type

Counseling

Font styles to use
Serif
Sans Serif
Other font styles liked:
• Audrey

Colors

Designer to choose colors to be used in the design.

Requirements
Must have
• Logo for Kindred Hearth. Color scheme that is complementary to the tree artwork provided. Font that incorporates or complements the font in the logo - Audrey. Photo of Gus & Norah with their bio (use a placeholder for now). Please include at least one or two stock photos of married couples somewhere in the brochure. See the examples in the creative brief and please let me know if you need me to provide the actual files (if you do not have access to Quillon Images).
Nice to have
• A design option that includes an infographic/icon style for me to consider. See creative brief document for more on this idea.
Should not have
• Note: I removed the prior instructions indicating this design should not have a full page bleed. That is no longer a limitation on this design. Feel free to go with what you think looks best to make your submission as strong as possible.

```html
<!DOCTYPE html>
<html lang="en">
<head>
<meta charset="utf-8">
<title>Kindred Hearth – Retreat Brochure</title>
<link href="https://fonts.googleapis.com/css2?family=Marcellus&family=Open+Sans:ital,wght@0,400;0,600;0,700;1,400&display=swap" rel="stylesheet">
<style>
:root{
  --bg:#d3d4d6;
  --sage:#a7b36f;
  --forest:#4f7a48;
  --forest-deep:#3f6a3a;
  --bark:#6b5428;
  --ink:#454545;
  --muted:#6a6a6a;
  --paper:#ffffff;
}
*{margin:0;padding:0;box-sizing:border-box}
html,body{width:886px;height:1200px;overflow:hidden}
body{background:var(--bg);font-family:"Open Sans",sans-serif;color:var(--ink);position:relative}
.spread{position:absolute;left:36px;width:821px;background:var(--paper);overflow:hidden}
.spread--outer{top:48px;height:537px}
.spread--inner{top:623px;height:534px}
.abs{position:absolute}
.curves{position:absolute;left:0;top:0}

/* agenda */
.agenda{left:0;top:0;width:411px;height:183px;background:var(--sage);color:#fff}
.agenda h3{position:absolute;top:16px;width:100%;text-align:center;font:400 12px "Marcellus",serif;letter-spacing:.5px}
.day{position:absolute;top:40px;width:110px}
.day-pill{height:12px;border-radius:7px;background:#fff;color:var(--ink);font-size:6.5px;text-align:center;line-height:12px;box-shadow:0 1px 2px rgba(0,0,0,.25)}
.day ul{list-style:none;margin-top:12px;font-size:6.4px;line-height:9.3px}
.day li{position:relative;padding-left:7px}
.day li::before{content:"";position:absolute;left:0;top:3px;width:3.5px;height:3.5px;border-radius:50%;background:#fff}
.agenda-note{position:absolute;top:169px;width:100%;text-align:center;font-size:5.4px}

.invest-title{left:21px;top:238px;font:400 18px "Marcellus",serif;color:var(--forest);letter-spacing:1px}
.brandmark{display:flex;flex-direction:column;align-items:center;gap:6px;color:var(--bark);font-family:"Marcellus",serif;text-align:center}
.brandmark .dot{border-radius:50%;background:var(--sage)}
.contact{left:164px;top:297px;width:230px;font-size:8px;line-height:12.5px;text-align:justify}
.contact p+p{margin-top:12px}
.contact strong{font-weight:700}

.photo{background:linear-gradient(160deg,#dfe6cf 0%,#b9c98f 35%,#8ea35c 70%,#6f8a45 100%)}
.footnotes{left:80px;top:463px;width:260px;text-align:center;color:#fff;font-size:5.3px;line-height:9.2px}
.cover-title{left:440px;top:458px;width:380px;text-align:center;color:#fff}
.cover-title h1{font:400 26px "Marcellus",serif;letter-spacing:1.5px;text-shadow:0 1px 3px rgba(0,0,0,.25)}
.cover-title p{font-size:12px;margin-top:6px}

/* inner spread */
.couple-photo{left:0;top:0;width:411px;height:232px;background:linear-gradient(120deg,#e9e7e2 0%,#cfd6df 40%,#9aa8bd 65%,#6c6a68 100%)}
.risk-band{left:0;top:127px;width:411px;height:15px;background:rgba(255,255,255,.85)}
.risk-title{left:22px;top:128px;font:400 11.5px "Marcellus",serif;color:var(--bark);letter-spacing:.6px}
.stat{left:22px;width:380px;height:10px;display:flex;align-items:center}
.stat-bar{width:140px;height:10px;border-radius:5px;background:var(--sage);position:relative;overflow:hidden}
.stat-fill{position:absolute;left:0;top:0;bottom:0;background:var(--forest);color:#fff;font:700 7px "Marcellus",serif;padding-left:6px;line-height:10px}
.stat-text{margin-left:10px;flex:1;height:10px;background:rgba(255,255,255,.85);font-size:6px;line-height:10px;padding-left:8px;color:var(--ink)}

.section-title{font:400 12.5px "Marcellus",serif;color:var(--bark);letter-spacing:.6px}
.invite-title{left:0;width:411px;top:268px;text-align:center}
.invite-lead{left:40px;width:331px;top:290px;text-align:center;font-size:7.8px;line-height:12px}
.pillar{top:338px;width:116px;height:77px;border:1px solid var(--forest);border-radius:6px;background:#fff}
.pillar-head{height:24px;margin:-1px -1px 0;background:var(--forest-deep);border-radius:6px 6px 4px 4px;color:#fff;font-size:7px;display:flex;align-items:center;justify-content:center;text-align:center;line-height:9px;box-shadow:0 1px 3px rgba(0,0,0,.3)}
.pillar p{font-size:8px;line-height:11px;text-align:center;color:var(--muted);padding:7px 12px 0}
.plus{top:344px;color:var(--forest);font-size:8px;font-weight:700}
.invite-body{left:22px;width:370px;top:438px;text-align:center;font-size:8.2px;line-height:14px}

.retreat-band{left:411px;top:0;width:410px;height:130px;background:var(--sage)}
.retreat-title{left:411px;width:410px;top:28px;text-align:center;color:#fff;font:400 13px "Marcellus",serif;letter-spacing:.6px}
.retreat-lead{left:411px;width:410px;top:56px;text-align:center;color:#fff;font-size:10.2px;line-height:14px}
.host-photo{left:421px;top:98px;width:118px;height:150px;background:linear-gradient(180deg,#b8b0a6 0%,#8d8782 55%,#3d4450 100%);border:1px solid #fff}
.hosts-title{left:552px;top:158px}
.hosts-bio{left:552px;top:178px;width:245px;font-size:6.9px;line-height:9.3px;text-align:justify}
.hosts-bio strong{font-weight:700}
.transform-title{left:411px;width:410px;top:272px;text-align:center}
.quote{width:182px;height:54px;border:1px solid #8a8a8a;border-radius:3px;padding:10px 5px 0}
.quote::before{content:"\201C\201C";position:absolute;top:-10px;left:50%;transform:translateX(-50%);background:#fff;padding:0 4px;font:700 18px/16px "Marcellus",serif;color:var(--bark);letter-spacing:-3px}
.quote p{font-size:5.6px;line-height:7.6px;font-style:italic;color:var(--muted);text-align:justify}
</style>
</head>
<body>

<section class="spread spread--outer">
  <div class="abs agenda">
    <h3>SAMPLE AGENDA</h3>
    <div class="day" style="left:22px">
      <div class="day-pill">Day One</div>
      <ul><li>Arrive, settle in, get acquainted</li><li>Individual reflection and<br>couple connection</li><li>Lunch</li><li>Session 1*</li><li>Break</li><li>Session 2</li><li>Free time</li><li>Dinner</li><li>5 minute huddle</li></ul>
    </div>
    <div class="day" style="left:151px">
      <div class="day-pill">Day Two</div>
      <ul><li>Coffee, individual reflection,<br>time with God</li><li>Breakfast</li><li>Couple breakout</li><li>Session 3</li><li>Break</li><li>Lunch</li><li>Sessions 4 &amp; 5: Building Bridges</li><li>Dinner date (couple only)</li><li>5 minute huddle</li></ul>
    </div>
    <div class="day" style="left:280px">
      <div class="day-pill">Day Three</div>
      <ul><li>Coffee, individual reflection<br>and time with God</li><li>Breakfast</li><li>Session 6: Integrated Intimacy</li><li>Lunch</li><li>Break</li><li>Session 7</li><li>Wrap up, next steps</li><li>Pray</li><li>Depart</li></ul>
    </div>
    <p class="agenda-note">* Each session lasts approximately 2 hours and includes time with the hosts and breakouts for reflection and exercises.</p>
  </div>

  <h2 class="abs invest-title">READY TO INVEST IN YOUR MARRIAGE?</h2>
  <div class="abs brandmark" style="left:18px;top:288px;width:110px">
    <span class="dot" style="width:46px;height:46px"></span>
    <span style="font-size:14px">Kindred Hearth</span>
  </div>
  <div class="abs contact">
    <p>Contact Gus &amp; Norah Hollis to request a confidential initial consultation: <strong>info@kindredhearthretreat.com</strong></p>
    <p>Retreat expenses are covered for you – including meals, lodging, teaching and materials. Couples are responsible for their own transportation to the retreat and childcare, if needed. Additional scholarships are available.</p>
  </div>

  <div class="abs photo" style="left:411px;top:110px;width:410px;height:340px" role="img" aria-label="Photo: close-up of an older couple holding hands over a sunlit green meadow"></div>

  <svg class="curves" width="821" height="537" viewBox="0 0 821 537" aria-hidden="true">
    <path d="M411 108 Q560 170 821 178 L821 0 L411 0 Z" fill="#fff"/>
    <path d="M411 108 Q560 170 821 178" fill="none" stroke="#a7b36f" stroke-width="7"/>
    <path d="M411 118 Q560 180 821 185" fill="none" stroke="#e4e4e4" stroke-width="3"/>
    <path d="M0 448 Q400 418 821 420 L821 537 L0 537 Z" fill="#6b5428"/>
    <path d="M0 455 Q400 428 821 434 L821 537 L0 537 Z" fill="#4f7a48"/>
  </svg>

  <div class="abs brandmark" style="left:645px;top:40px;width:140px">
    <span class="dot" style="width:60px;height:60px"></span>
    <span style="font-size:17px">Kindred Hearth</span>
  </div>
  <div class="abs footnotes">
    ¹The Ashgrove Institute, 2006.<br>²The Fenwick Group, The State of Pastors, 2017.<br>Testimonials have been edited for clarity and confidentiality.<br>Tree artwork by Mara Ellison. Photo of Hollises by Lindell Studio Photography.<br>©Gus and Norah Hollis.
  </div>
  <div class="abs cover-title">
    <h1>KINDRED HEARTH</h1>
    <p>A Personalized Retreat for Couples in Ministry</p>
  </div>
</section>

<section class="spread spread--inner">
  <div class="abs couple-photo" role="img" aria-label="Photo: a young married couple seated on a sofa, talking and holding hands"></div>
  <div class="abs risk-band"></div>
  <h3 class="abs risk-title">MINISTRY MARRIAGES ARE AT RISK</h3>
  <div class="abs stat" style="top:156px"><div class="stat-bar"><div class="stat-fill" style="width:77%">77%</div></div><div class="stat-text">of pastors feel they do not have a good marriage¹</div></div>
  <div class="abs stat" style="top:171px"><div class="stat-bar"><div class="stat-fill" style="width:48%">48%</div></div><div class="stat-text">say their current ministry role has been difficult on their marriage²</div></div>
  <div class="abs stat" style="top:186px"><div class="stat-bar"><div class="stat-fill" style="width:26%">26%</div></div><div class="stat-text">of pastors face significant marital problems²</div></div>

  <div class="abs retreat-band"></div>
  <svg class="curves" width="821" height="534" viewBox="0 0 821 534" aria-hidden="true">
    <path d="M0 240 L0 212 Q200 208 411 190 L411 240 Z" fill="#fff"/>
    <path d="M0 210 Q200 205 411 190" fill="none" stroke="#a7b36f" stroke-width="3"/>
    <path d="M0 218 Q200 212 411 196" fill="none" stroke="#6b5428" stroke-width="4"/>
    <path d="M411 150 Q620 115 821 112 L821 140 L411 140 Z" fill="#fff"/>
    <path d="M530 155 Q680 116 821 112" fill="none" stroke="#fff" stroke-width="6"/>
    <path d="M530 162 Q680 124 821 122" fill="none" stroke="#6b5428" stroke-width="4"/>
    <path d="M0 522 Q400 492 821 496 L821 534 L0 534 Z" fill="#6b5428"/>
    <path d="M0 528 Q400 500 821 505 L821 534 L0 534 Z" fill="#4f7a48"/>
  </svg>
  <div class="abs" style="left:411px;top:164px;width:410px;height:20px;background:#fff"></div>

  <h2 class="abs retreat-title">A RETREAT FOR COUPLES IN MINISTRY</h2>
  <p class="abs retreat-lead">Kindred Hearth retreats provide you time, space,<br>and Bible-based tools to cultivate a life-giving marriage.</p>
  <div class="abs host-photo" role="img" aria-label="Photo placeholder: hosts Gus and Norah Hollis standing together"></div>
  <h3 class="abs section-title hosts-title">YOUR HOSTS</h3>
  <p class="abs hosts-bio"><strong>Gus and Norah Hollis</strong> bring more than 20 years of experience helping build and restore Christ-centered marriages. They have experienced God’s redemption in their own broken stories. A compassionate and insightful listener, Gus is a retired energy industry leader currently serving on a corporate board and church overseer board. Norah formerly served in full-time ministry and is a gifted teacher who delights in unpacking God’s truth. God has used the time and tools they offer to transform many marriages.</p>

  <h3 class="abs section-title invite-title">YOUR INVITATION</h3>
  <p class="abs invite-lead">Whether your marriage is thriving, in distress, or needs a fresh start, Kindred Hearth retreats equip couples in ministry to:</p>
  <div class="abs pillar" style="left:22px"><div class="pillar-head">DEEPEN INTIMACY</div><p>Reinvigorate love by being heard and valued</p></div>
  <span class="abs plus" style="left:141px">+</span>
  <div class="abs pillar" style="left:150px"><div class="pillar-head">UNTANGLE<br>RELATIONAL KNOTS</div><p>Heal hurts, care for yourself and each other with grace</p></div>
  <span class="abs plus" style="left:269px">+</span>
  <div class="abs pillar" style="left:278px"><div class="pillar-head">REPLENISH JOY</div><p>Create an environment to grow and rediscover fun</p></div>
  <p class="abs invite-body">The 3-day retreat is personally tailored for one couple only. We provide a lovely, comfortable, private and safe setting where everything is taken care of. We can welcome you to our locations in Austin and Chicago or – in special circumstances – bring the retreat to your area.</p>

  <h3 class="abs section-title transform-title">EXPERIENCE TRANSFORMATION</h3>
  <div class="abs quote" style="left:421px;top:298px"><p>Our marriage was in crisis. The stress of ministry had taken a deep toll on us and in the worst moments we didn’t even like each other anymore. Gus and Norah are people we trust with the darkest moments of our lives. They stood with us and held up our arms to allow us to continue.</p></div>
  <div class="abs quote" style="left:614px;top:298px"><p>Gus and Norah meet people in their pain and brokenness without shame or judgment and gently help them make major shifts from a place of extreme distress to a hopeful and productive path forward.</p></div>
  <div class="abs quote" style="left:421px;top:366px"><p>During a critical time, Gus and Norah helped us navigate our marriage around the traps that we so easily and repeatedly fell into… We were sitting ducks for the evil one… They took us to the deep end of the marriage pool and dove in first. I see a more fruitful and God honoring marriage ahead.</p></div>
  <div class="abs quote" style="left:614px;top:366px"><p>Gus and Norah understand the sanctity of safely and compassionately learning from each other’s stories…the triumphs, the failures, the times of healing, and the times of deep woundedness. They hold the stories of the couples they work tenderly, confidentially and dearly.</p></div>
  <div class="abs quote" style="left:421px;top:434px"><p>This experience was the most important thing I have ever done in my life outside of saying yes to Jesus. As a pastor, I have always known that my family is my number one ministry. This experience helped me take that theoretical goal and turn it into a reality.</p></div>
  <div class="abs quote" style="left:614px;top:434px"><p>Gus and Norah exemplify these qualities: a safety zone with in-the-vault assurance, advice grounded in scripture, a straightforward message, truth spoken in love even when painful, vulnerability and authenticity.</p></div>
</section>

</body>
</html>
```